Website Design for BRAVO FREIGHTWAY

Hello. We are a Freight Brokage business in the transportation and logistics industry in the USA. Company name is BRAVO FREIGHTWAY. I'm looking to have a 5 page or less website built. Must have HOME, SHIPPERS, CARRIERS, ABOUT and CONTACT US.. I have additional information that needs to be placed in the footer of the website. Company address, contact info privacy and terms and conditions Need nice, vibrant looking site. The website needs to be a fully functionable site that is built and coded for wordpress and ready for hosting. Please visit these link for you to have an idea of the look and feel I want. www.tallowcargo.example www.pinecrest-haulage.example. Will have logo concept in 2 days for upload. As time goes by I will supply more content and the layout of the respective pages.

```html
<!DOCTYPE html>
<html lang="en">
<head>
<meta charset="utf-8">
<title>Bravo Freightway</title>
<link href="https://fonts.googleapis.com/css2?family=Oswald:wght@400;500;600&family=Roboto:wght@400;500;700&display=swap" rel="stylesheet">
<style>
:root{
  --blue:#0d4ea6;
  --navy:#1f3d6e;
  --band:#2c5a94;
  --ink:#111418;
  --text:#3a3f47;
  --card:#e6f0fa;
  --pale:#f1f6fc;
  --field:#f1f1f3;
  --white:#fff;
  --footer:#121212;
}
*{box-sizing:border-box;margin:0;padding:0}
html,body{width:1200px;height:3720px;overflow:hidden}
body{position:relative;font-family:'Roboto',sans-serif;color:var(--text);background:var(--white)}
.abs{position:absolute}
.head{font-family:'Oswald',sans-serif;font-weight:500;color:var(--ink);text-transform:uppercase;letter-spacing:.5px}
.head span{color:var(--blue)}
.underline{position:absolute;height:4px;width:64px;background:var(--blue)}
.btn{position:absolute;display:flex;align-items:center;justify-content:center;gap:8px;border-radius:24px;background:var(--blue);color:var(--white);font-weight:700;font-size:16px;text-transform:uppercase}
.btn .dot{width:15px;height:15px;border-radius:50%;background:currentColor;position:relative}
.btn .dot::after{content:"";position:absolute;left:5px;top:4px;border:4px solid transparent;border-left:5px solid var(--blue);border-right:0}
.btn.light{background:var(--white);color:var(--blue)}
.btn.light .dot::after{border-left-color:var(--white)}

/* header */
.site-header{position:absolute;left:0;top:0;width:1200px;height:82px;background:var(--white);z-index:3}
.brand{position:absolute;left:110px;top:24px;display:flex;align-items:center;gap:12px}
.brand .mark{width:34px;height:34px;border-radius:50%;background:var(--blue)}
.brand .name{font-family:'Oswald',sans-serif;font-weight:500;font-size:26px;color:var(--navy)}
.nav{position:absolute;left:462px;top:30px;display:flex;gap:28px;font-size:15px;font-weight:500;color:var(--ink)}
.nav .active{color:var(--blue)}
.login{left:962px;top:21px;width:118px;height:38px;font-size:15px;font-weight:500}

/* hero */
.hero-edge{left:0;top:82px;width:1200px;height:700px;background:var(--navy);clip-path:polygon(0 0,100% 0,100% 537px,357px 698px,0 543px)}
.hero-photo{left:0;top:82px;width:1200px;height:700px;background:linear-gradient(160deg,#c98a3a 0%,#8a6a3e 22%,#4d4a3a 45%,#2a2d33 70%,#3a3d44 100%);clip-path:polygon(0 0,100% 0,100% 537px,357px 680px,0 546px)}
.hero-title{left:119px;top:278px;color:var(--white);font-family:'Oswald',sans-serif;font-weight:500;text-transform:uppercase}
.hero-title .small{font-size:40px;line-height:46px}
.hero-title .big{font-size:68px;line-height:84px;font-weight:600}
.hero-copy{left:119px;top:418px;width:440px;color:var(--white);font-size:17px;line-height:27px;font-weight:500}
.get-started{left:119px;top:497px;width:188px;height:46px}
.slide-arrow{width:40px;height:40px;border-radius:50%;background:rgba(255,255,255,.25);border:1px solid rgba(255,255,255,.4)}
.slide-arrow svg{display:block;margin:11px auto}

/* services */
.services-bg{left:0;top:760px;width:1200px;height:620px;background:linear-gradient(180deg,#fff 0%,#f4f8fc 60%,#fff 100%)}
.card{position:absolute;top:975px;width:236px;height:308px;background:var(--card);border-radius:4px;text-align:center;padding:40px 22px 0}
.card.active{background:linear-gradient(180deg,#2c5f9f,#1e4f8e);border-bottom:3px solid #2f8de0}
.card .icon{width:88px;height:88px;border-radius:50%;background:#3073c0;margin:0 auto 28px;display:flex;align-items:center;justify-content:center}
.card.active .icon{background:var(--white)}
.card h3{font-size:17px;font-weight:500;color:var(--ink);line-height:24px;margin-bottom:4px}
.card p{font-size:15px;line-height:25px;color:var(--text)}
.card.active h3,.card.active p{color:var(--white)}
.side-arrow{position:absolute;top:1122px}

/* about */
.about-photo{left:0;top:1378px;width:635px;height:458px;background:linear-gradient(135deg,#dfe5ea 0%,#c2cbd4 40%,#8a8f8a 75%,#b8a78d 100%);clip-path:polygon(0 0,530px 0,635px 100%,0 100%)}
.body-copy{font-size:15px;line-height:26px;text-align:justify}

/* carriers */
.carriers{left:0;top:1836px;width:1200px;height:379px;background:linear-gradient(90deg,#2a558e,#2f5f9b 50%,#2a558e);text-align:center;color:var(--white)}

/* shippers */
.shippers-bg{left:0;top:2215px;width:1200px;height:468px;background:var(--pale)}
.shippers-photo{left:565px;top:2215px;width:635px;height:468px;background:linear-gradient(120deg,#6a3a34 0%,#8a2b2e 35%,#5a4c3c 65%,#2f3442 100%);clip-path:polygon(100px 0,100% 0,100% 100%,0 100%)}

/* contact */
.contact-bg{left:0;top:2683px;width:1200px;height:700px;background:linear-gradient(180deg,#fff 0%,#f7f9fb 100%)}
.field{position:absolute;background:var(--field);border:1px solid #dcdde2;border-radius:28px;font-size:14px;color:#8c9099;padding:0 26px;display:flex;align-items:center}
.field.area{border-radius:26px;align-items:flex-start;padding-top:24px}

/* footer */
.footer{left:0;top:3225px;width:1200px;height:495px}
.footer h4{position:absolute;font-size:17px;font-weight:700;color:var(--white);text-transform:uppercase;top:3397px}
.flink{position:absolute;left:399px;font-size:12px;color:var(--white)}
.finfo{position:absolute;left:575px;display:flex;align-items:center;gap:12px;font-size:12px;line-height:20px;color:var(--white)}
.finfo .ic{width:26px;height:26px;border-radius:50%;background:var(--white);flex:none;display:flex;align-items:center;justify-content:center}
.social{position:absolute;top:3569px;width:30px;height:30px;border-radius:50%;background:var(--white)}
.social.blue{background:var(--blue)}
.bottom-bar{left:0;top:3660px;width:1200px;height:60px;background:#0a0a0a;color:var(--white);font-size:14px}
</style>
</head>
<body>

<header class="site-header">
  <div class="brand"><div class="mark"></div><div class="name">BRAVO FREIGHTWAY</div></div>
  <nav class="nav"><span class="active">&#10148; HOME</span><span>SHIPPERS</span><span>CARRIERS</span><span>ABOUT</span><span>CONTACT US</span></nav>
  <div class="btn login">LOGIN &nbsp;<svg width="12" height="13" viewBox="0 0 12 13"><circle cx="6" cy="3.5" r="3" fill="#fff"/><path d="M0 13c0-4 2.5-6 6-6s6 2 6 6z" fill="#fff"/></svg></div>
</header>

<section class="hero">
  <div class="abs hero-edge"></div>
  <div class="abs hero-photo" role="img" aria-label="Dark blue semi truck on a desert road with orange hillside at sunset"></div>
  <div class="abs hero-title"><div class="small">WELCOME TO</div><div class="big">BRAVO FREIGHTWAY</div></div>
  <p class="abs hero-copy">Lorem ipsum dolor sit amet, consectetur adipiscing elit, tempor incididunt labore dolore magna aliqua.</p>
  <div class="btn get-started">GET STARTED <span class="dot"></span></div>
  <div class="abs slide-arrow" style="left:35px;top:394px"><svg width="12" height="18"><path d="M10 1L2 9l8 8" stroke="#fff" stroke-width="2" fill="none"/></svg></div>
  <div class="abs slide-arrow" style="left:1124px;top:394px"><svg width="12" height="18"><path d="M2 1l8 8-8 8" stroke="#fff" stroke-width="2" fill="none"/></svg></div>
</section>

<section class="services">
  <div class="abs services-bg"></div>
  <h2 class="abs head" style="left:0;width:1200px;top:855px;text-align:center;font-size:42px">LTL FREIGHT <span>MOVEMENT</span></h2>
  <div class="underline" style="left:578px;top:912px"></div>

  <svg class="side-arrow" style="left:38px" width="14" height="24"><path d="M12 2L3 12l9 10" stroke="#111" stroke-width="2.5" fill="none"/></svg>
  <svg class="side-arrow" style="left:1148px" width="14" height="24"><path d="M2 2l9 10-9 10" stroke="#111" stroke-width="2.5" fill="none"/></svg>

  <div class="card" style="left:94px">
    <div class="icon"><svg width="46" height="46" viewBox="0 0 46 46" fill="none" stroke="#fff" stroke-width="2"><path d="M8 12h22l6 6h4M18 6l6 6"/><rect x="6" y="26" width="20" height="12"/><path d="M26 30h8l5 5v3H26"/><circle cx="12" cy="40" r="3"/><circle cx="32" cy="40" r="3"/></svg></div>
    <h3>National And Regional Capacity</h3>
    <p>Direct access to over 100 national, regional, and local LTL carriers.</p>
  </div>
  <div class="card active" style="left:353px">
    <div class="icon"><svg width="50" height="50" viewBox="0 0 50 50" fill="none" stroke="#1f4f8e" stroke-width="2"><rect x="13" y="4" width="24" height="16" rx="2"/><path d="M18 10h14M18 14h10"/><circle cx="10" cy="32" r="4"/><circle cx="25" cy="32" r="4"/><circle cx="40" cy="32" r="4"/><path d="M3 46c0-6 3-9 7-9s7 3 7 9M18 46c0-6 3-9 7-9s7 3 7 9M33 46c0-6 3-9 7-9s7 3 7 9"/></svg></div>
    <h3>Dedicated Representatives</h3>
    <p>A dedicated representative that knows your business and can easily troubleshoot shipment issues without your</p>
  </div>
  <div class="card" style="left:611px">
    <div class="icon"><svg width="48" height="48" viewBox="0 0 48 48" fill="none" stroke="#fff" stroke-width="2"><circle cx="10" cy="10" r="4"/><circle cx="38" cy="10" r="4"/><circle cx="10" cy="34" r="4"/><circle cx="38" cy="34" r="4"/><rect x="17" y="16" width="14" height="10" rx="2"/><path d="M4 46c0-5 3-7 6-7s6 2 6 7M32 46c0-5 3-7 6-7s6 2 6 7"/></svg></div>
    <h3>Proactive Communication</h3>
    <p>Proactive communication with LTL carriers, problem resolutions, and unparalleled knowledge of the LTL</p>
  </div>
  <div class="card" style="left:870px">
    <div class="icon"><svg width="46" height="46" viewBox="0 0 46 46" fill="none" stroke="#fff" stroke-width="2"><rect x="8" y="4" width="24" height="34" rx="2"/><path d="M13 12h14M13 18h14M13 24h8"/><circle cx="30" cy="30" r="7"/><path d="M35 35l7 7"/></svg></div>
    <h3>Accessorial Verification</h3>
    <p>Our trams provide verification of shipper and receiver premises toz make sure your shipment doesn't require any</p>
  </div>
</section>

<section class="about">
  <div class="abs about-photo" role="img" aria-label="White semi trucks parked in a row with a smiling driver holding paperwork"></div>
  <svg class="abs" style="left:530px;top:1378px" width="80" height="260"><path d="M6 0L74 254" stroke="#0d4ea6" stroke-width="7"/></svg>
  <h2 class="abs head" style="left:687px;top:1432px;font-size:42px">ABOUT <span>US</span></h2>
  <div class="underline" style="left:687px;top:1484px"></div>
  <p class="abs body-copy" style="left:687px;top:1524px;width:427px">Lorem ipsum dolor sit amet, consectetur adipiscing elit, sed do eiusmod tempor incididunt ut labore et dolore magna aliqua. Ut enim ad minim veniam, quis nostrud exercitation ullamco laboris nisi ut aliquip ex ea commodo consequat.</p>
  <p class="abs body-copy" style="left:687px;top:1644px;width:427px">Duis aute irure dolor in reprehenderit in voluptate velit esse cillum culpa qui officia deserunt mollit anim id est laborum.</p>
  <div class="btn" style="left:687px;top:1728px;width:172px;height:42px">READ MORE <span class="dot"></span></div>
</section>

<section class="abs carriers">
  <h2 class="head" style="color:#fff;font-size:40px;margin-top:56px">OUR CARRIERS</h2>
  <p style="width:940px;margin:22px auto 0;font-size:15px;line-height:27px">Sed ut perspiciatis unde omnis iste natus error sit voluptatem accusantium doloremque laudantium, totam rem aperiam, eaque ipsa quae ab illo inventore veritatis et quasi architecto beatae vitae dicta sunt explicabo. Nemo enim ipsam voluptatem quia voluptas sit aspernatur aut odit aut fugit, sed quia consequuntur magni dolores eos qui ratione voluptatem sequi nesciunt. Neque porro non numquam eius modi tempora incidunt ut quis nostrum exercitationem ullam labore et dolore magnam aliquam quaerat voluptatem.</p>
  <div class="btn light" style="left:505px;top:281px;width:188px;height:45px">LEARN MORE <span class="dot"></span></div>
</section>

<section class="shippers">
  <div class="abs shippers-bg"></div>
  <div class="abs shippers-photo" role="img" aria-label="Two truck drivers in caps standing with arms crossed in front of red trucks"></div>
  <svg class="abs" style="left:596px;top:2215px" width="74" height="230"><path d="M70 0L4 226" stroke="#0d4ea6" stroke-width="7"/></svg>
  <h2 class="abs head" style="left:112px;top:2268px;font-size:42px">OUR SHIPPERS</h2>
  <div class="underline" style="left:112px;top:2320px"></div>
  <p class="abs body-copy" style="left:112px;top:2360px;width:427px;color:var(--ink)">Lorem ipsum dolor sit amet, consectetur adipiscing elit, sed do eiusmod tempor incididunt ut labore et dolore magna aliqua. Ut enim ad minim veniam, quis nostrud exercitation ullamco laboris nisi ut aliquip ex ea commodo consequat.</p>
  <p class="abs body-copy" style="left:112px;top:2480px;width:427px;color:var(--ink)">Duis aute irure dolor in reprehenderit in voluptate velit esse cillum culpa qui officia deserunt mollit anim id est laborum.</p>
  <div class="btn" style="left:112px;top:2567px;width:172px;height:43px">READ MORE <span class="dot"></span></div>
</section>

<section class="contact">
  <div class="abs contact-bg"></div>
  <h2 class="abs head" style="left:0;width:1200px;top:2754px;text-align:center;font-size:42px">CONTACT <span>US</span></h2>
  <div class="underline" style="left:566px;top:2808px;width:72px"></div>
  <div class="field" style="left:193px;top:2873px;width:394px;height:54px">Name</div>
  <div class="field" style="left:197px;top:2943px;width:394px;height:54px">Email Address</div>
  <div class="field" style="left:197px;top:3008px;width:394px;height:54px">Phone Number</div>
  <div class="field area" style="left:610px;top:2873px;width:396px;height:186px">Message</div>
  <div class="btn" style="left:500px;top:3110px;width:206px;height:52px;font-size:17px;border-radius:26px">SUBMIT NOW <span class="dot"></span></div>
</section>

<footer class="abs footer">
  <svg class="abs" style="left:0;top:0" width="1200" height="495"><polygon points="0,155 826,0 1200,150 1200,495 0,495" fill="#2c5a94"/><polygon points="0,165 826,30 1200,160 1200,495 0,495" fill="var(--footer)"/></svg>
</footer>
<div class="abs" style="left:83px;top:3480px;display:flex;align-items:center;gap:10px"><div style="width:30px;height:30px;border-radius:50%;background:var(--blue)"></div><div style="font-family:'Oswald',sans-serif;font-weight:500;font-size:25px;color:#fff">BRAVO FREIGHTWAY</div></div>

<h4 style="left:399px">Quick Links</h4>
<div class="flink" style="top:3455px">Home</div>
<div class="flink" style="top:3488px">Shippers</div>
<div class="flink" style="top:3520px">Carriers</div>
<div class="flink" style="top:3553px">About</div>
<div class="flink" style="top:3585px">Contact Us</div>

<h4 style="left:575px">Contact Us</h4>
<div class="finfo" style="top:3457px"><span class="ic"><svg width="12" height="12" viewBox="0 0 12 12"><path d="M2 1l2 0 1 3-1.5 1a7 7 0 0 0 3.5 3.5L8 7l3 1v2a1 1 0 0 1-1 1C5 11 1 7 1 2a1 1 0 0 1 1-1z" fill="#0d4ea6"/></svg></span>1-800-555-0147</div>
<div class="finfo" style="top:3498px"><span class="ic"><svg width="12" height="10"><rect x="0.5" y="0.5" width="11" height="9" fill="#0d4ea6"/><path d="M1 1l5 4 5-4" stroke="#fff" fill="none"/></svg></span>support@bravofreightway.example</div>
<div class="finfo" style="top:3532px"><span class="ic"><svg width="10" height="13" viewBox="0 0 10 13"><path d="M5 13S0 7 0 5a5 5 0 0 1 10 0c0 2-5 8-5 8z" fill="#0d4ea6"/><circle cx="5" cy="5" r="2" fill="#fff"/></svg></span><span>Bravo Freightway, LLC 410 N Harbor Way<br>Suite 210 Fairview, OR 97000</span></div>
<div class="finfo" style="top:3593px"><span class="ic"><svg width="12" height="12"><rect x="1" y="1" width="10" height="10" rx="1" fill="#0d4ea6"/><rect x="3" y="3" width="6" height="3" fill="#fff"/></svg></span>503-555-0182</div>

<h4 style="left:844px">Subscribe To Our Blog</h4>
<p class="abs" style="left:844px;top:3453px;width:240px;font-size:11.5px;line-height:20px;color:#fff">Sign up today to get resources on how to attract and retain more customers!</p>
<div class="abs" style="left:844px;top:3509px;width:253px;height:36px;border-radius:18px;background:#fff;display:flex;align-items:center;padding-left:14px;font-size:10px;color:#777;overflow:hidden">&#9993;&nbsp; Email Address<span style="position:absolute;right:0;top:0;width:48px;height:36px;background:var(--blue);display:flex;align-items:center;justify-content:center"><svg width="16" height="14"><path d="M0 7L16 0 12 14 8 9z" fill="#fff"/></svg></span></div>
<div class="social" style="left:846px"></div>
<div class="social blue" style="left:885px"></div>
<div class="social" style="left:924px"></div>
<div class="social" style="left:963px"></div>

<div class="abs bottom-bar">
  <span class="abs" style="left:124px;top:21px">Copyright© 2023 &nbsp;<u>Bravo Freightway.</u> &nbsp;| &nbsp;All Rights Reserved</span>
  <span class="abs" style="left:879px;top:21px">Privacy and Terms and Conditions</span>
</div>

</body>
</html>
```